Taste of Kerwin digital board & Corflute design

Hi, we are a restaurant based in Parramatta (NSW). We are looking forward for a creative design for our menu to attract the customers at our two different locations.
1. We need a 80 x 296 cm digital board design for display of menu items.
few of the drafts are attached to provide a reference. However, we would request not the similar ones but certain novel and creative designs.
2. We need 3 different 900x1200mm 'A-Frame' or Corflute designs to
-- display our opening hours and details
-- display our flagship items of chaat counter(lassa thali)
--display our menu for TOK, Brindlemarts
--display our menu for TOK, Harrowgate.

```html
<!DOCTYPE html>
<html lang="en">
<head>
<meta charset="utf-8">
<title>Taste of Kerwin – Menu Board</title>
<link href="https://fonts.googleapis.com/css2?family=Roboto:wght@500;700&family=Oswald:wght@300;400;500&display=swap" rel="stylesheet">
<style>
  :root{
    --bg-stone:#e7e7e8;
    --bg-stone-dark:#d9d9db;
    --band-orange:#f7871f;
    --band-orange-deep:#e0701a;
    --panel-maroon:#4a1519;
    --item-orange:#f5862b;
    --note-white:#f4eee9;
    --brand-ink:#1e1e1e;
    --momos:#6cb04f;
    --thali:#d8424a;
    --biryani:#3a9cc2;
    --curries:#c48c63;
    --street:#4d7d90;
    --drinks:#7c1a2e;
    --drinks-ring:#f2b232;
  }
  *{margin:0;padding:0;box-sizing:border-box}
  html,body{width:1200px;height:324px;overflow:hidden;background:var(--bg-stone)}
  .board{position:relative;width:1200px;height:324px;overflow:hidden;
    background:radial-gradient(ellipse at 30% 20%,var(--bg-stone) 0%,var(--bg-stone-dark) 100%);}
  .brand-disc{position:absolute;left:502px;top:-123px;width:196px;height:196px;border-radius:50%;background:#fff;z-index:1}
  .brand-name{position:absolute;left:502px;top:35px;width:196px;text-align:center;
    font:500 14.5px/1 "Roboto",sans-serif;color:var(--brand-ink);z-index:2;letter-spacing:-.2px}
  .category-title{position:absolute;top:57px;width:200px;text-align:center;
    font:700 19.5px/1 "Roboto",sans-serif;letter-spacing:.2px}
  .dish-ring{position:absolute;top:83px;width:148px;height:148px;border-radius:50%;border:6.5px solid}
  .dish-photo{position:absolute;inset:0;margin:2px;border-radius:50%}
  .band{position:absolute;left:0;width:1200px;z-index:3}
  .band-light{top:170px;height:18px;background:var(--band-orange);opacity:.88}
  .band-deep{top:188px;height:16px;background:var(--band-orange-deep);opacity:.9}
  .menu-panel{position:absolute;left:0;top:204px;width:1200px;height:120px;background:var(--panel-maroon);z-index:4}
  .menu-list{position:absolute;top:12px;width:170px}
  .menu-item{display:flex;height:20px;align-items:center;
    font:400 14.5px/1 "Oswald",sans-serif;color:var(--item-orange);letter-spacing:.1px}
  .menu-item .name{width:104px;white-space:nowrap}
  .menu-item .price{white-space:nowrap}
  .menu-item .currency{font-weight:300;font-size:12px;margin-left:2px}
  .menu-note{font:300 11.5px/1 "Oswald",sans-serif;color:var(--note-white);height:18px;margin-top:-4px}
</style>
</head>
<body>
<main class="board">
  <div class="brand-disc"></div>
  <div class="brand-name">Taste of Kerwin</div>

  <h2 class="category-title" style="left:-1px;color:var(--momos)">MOMOS</h2>
  <h2 class="category-title" style="left:199px;color:var(--thali)">THALI</h2>
  <h2 class="category-title" style="left:399px;color:var(--biryani)">BIRYANI</h2>
  <h2 class="category-title" style="left:599px;color:var(--curries)">CURRIES</h2>
  <h2 class="category-title" style="left:800px;color:var(--street)">STREET FOOD</h2>
  <h2 class="category-title" style="left:1000px;color:var(--drinks)">DRINKS</h2>

  <div class="dish-ring" style="left:25px;border-color:var(--momos)">
    <div class="dish-photo" role="img" aria-label="Plate of steamed momos" style="background:radial-gradient(circle at 45% 45%,#f1ecd8,#d8cfa9 60%,#b9b08a)"></div></div>
  <div class="dish-ring" style="left:226px;border-color:var(--thali)">
    <div class="dish-photo" role="img" aria-label="Thali platter with curries and breads" style="background:radial-gradient(circle at 50% 55%,#c9a15a,#8a5a2a 55%,#2a1a14)"></div></div>
  <div class="dish-ring" style="left:426px;border-color:var(--biryani)">
    <div class="dish-photo" role="img" aria-label="Bowl of biryani" style="background:radial-gradient(circle at 50% 40%,#f0c24a,#d8962e 45%,#3aa3b8 80%)"></div></div>
  <div class="dish-ring" style="left:626px;border-color:var(--curries)">
    <div class="dish-photo" role="img" aria-label="Bowl of paneer curry" style="background:radial-gradient(circle at 55% 40%,#e0602a,#b9411c 45%,#3c4a52 80%)"></div></div>
  <div class="dish-ring" style="left:827px;border-color:var(--street)">
    <div class="dish-photo" role="img" aria-label="Pani puri with chutney" style="background:radial-gradient(circle at 45% 55%,#e3b36a,#c98b3e 55%,#e9e5dc)"></div></div>
  <div class="dish-ring" style="left:1027px;border-color:var(--drinks-ring)">
    <div class="dish-photo" role="img" aria-label="Glasses of mango lassi" style="background:radial-gradient(circle at 60% 50%,#f5c93a,#e8b42c 40%,#dcdad6 75%)"></div></div>

  <div class="band band-light"></div>
  <div class="band band-deep"></div>

  <section class="menu-panel">
    <div class="menu-list" style="left:28px">
      <div class="menu-item"><span class="name">Veg Momos</span><span class="price">0.00<span class="currency">$</span></span></div>
      <div class="menu-note">Steam or Fried</div>
      <div class="menu-item"><span class="name">Non-Veg Momos</span><span class="price">0.00<span class="currency">$</span></span></div>
      <div class="menu-note">Steam or Fried</div>
    </div>
    <div class="menu-list" style="left:228px">
      <div class="menu-item"><span class="name">Veg Thali</span><span class="price">0.00<span class="currency">$</span></span></div>
      <div class="menu-item"><span class="name">Non-Veg Thali</span><span class="price">0.00<span class="currency">$</span></span></div>
    </div>
    <div class="menu-list" style="left:428px">
      <div class="menu-item"><span class="name">Veg Biryani</span><span class="price">0.00<span class="currency">$</span></span></div>
      <div class="menu-item"><span class="name">Goat Biryani</span><span class="price">0.00<span class="currency">$</span></span></div>
      <div class="menu-item"><span class="name">Chicken Biryani</span><span class="price">0.00<span class="currency">$</span></span></div>
    </div>
    <div class="menu-list" style="left:628px">
      <div class="menu-item"><span class="name">Chicken Curry</span><span class="price">0.00<span class="currency">$</span></span></div>
      <div class="menu-item"><span class="name">Lamb Curry</span><span class="price">0.00<span class="currency">$</span></span></div>
      <div class="menu-item"><span class="name">Goat Curry</span><span class="price">0.00<span class="currency">$</span></span></div>
      <div class="menu-item"><span class="name">Paneer Curry</span><span class="price">0.00<span class="currency">$</span></span></div>
      <div class="menu-item"><span class="name">Dal</span><span class="price">0.00<span class="currency">$</span></span></div>
    </div>
    <div class="menu-list" style="left:828px">
      <div class="menu-item"><span class="name">Pani Puri</span><span class="price">0.00<span class="currency">$</span></span></div>
      <div class="menu-item"><span class="name">Chaat Papdi</span><span class="price">0.00<span class="currency">$</span></span></div>
      <div class="menu-item"><span class="name">Samosa Chaat</span><span class="price">0.00<span class="currency">$</span></span></div>
      <div class="menu-item"><span class="name">Bhelpuri</span><span class="price">0.00<span class="currency">$</span></span></div>
    </div>
    <div class="menu-list" style="left:1029px">
      <div class="menu-item"><span class="name">Mango Lassi</span><span class="price">0.00<span class="currency">$</span></span></div>
      <div class="menu-item"><span class="name">Masala Chai</span><span class="price">0.00<span class="currency">$</span></span></div>
    </div>
  </section>
</main>
</body>
</html>
```